Sleek, Professional Business Card Design Needed

Business Cards - Logo Attached.

We are a solar consulting company. We are national and want our cards to represent the professional high quality products that we offer.

Industry/Entity Type

Business

Contact Information for Business Card

n/a

Requirements
Must have
• Design
• Name
• Position
• Number
• Email
• Address
Should not have
• Not be too crowded

```html
<!DOCTYPE html>
<html lang="en">
<head>
<meta charset="UTF-8">
<title>Sunward Grid – Business Card</title>
<link href="https://fonts.googleapis.com/css2?family=Jost:wght@400;500&display=swap" rel="stylesheet">
<style>
  :root {
    --brand-blue: #0a8ac9;
    --brand-green: #9dc93b;
    --card-bg: #ffffff;
  }
  * { margin: 0; padding: 0; box-sizing: border-box; }
  html, body {
    width: 686px;
    height: 1200px;
    overflow: hidden;
    background: var(--card-bg);
  }
  .card {
    position: relative;
    width: 686px;
    height: 1200px;
    background: var(--card-bg);
    font-family: "Jost", "Futura", sans-serif;
    font-weight: 500;
    text-align: center;
  }
  .brand-mark {
    position: absolute;
    left: 235px;
    top: 52px;
    width: 216px;
    height: 216px;
  }
  .brand-name {
    position: absolute;
    left: 0;
    right: 0;
    top: 312px;
    font-size: 60px;
    line-height: 1;
    letter-spacing: 1px;
    color: var(--brand-blue);
    text-transform: uppercase;
  }
  .person-name {
    position: absolute;
    left: 0; right: 0;
    top: 533px;
    font-size: 50px;
    line-height: 1;
    color: var(--brand-green);
  }
  .person-position {
    position: absolute;
    left: 0; right: 0;
    top: 615px;
    font-size: 38px;
    line-height: 1;
    color: var(--brand-blue);
  }
  .rule {
    position: absolute;
    left: 111px;
    width: 465px;
    height: 5px;
  }
  .rule--blue { background: var(--brand-blue); }
  .rule--green { background: var(--brand-green); }
  .address {
    position: absolute;
    left: 0; right: 0;
    top: 752px;
    font-size: 38px;
    line-height: 45px;
    color: var(--brand-blue);
  }
  .phone {
    position: absolute;
    left: 0; right: 0;
    top: 989px;
    font-size: 34px;
    line-height: 1;
    color: var(--brand-green);
  }
  .email {
    position: absolute;
    left: 0; right: 0;
    top: 1101px;
    font-size: 34px;
    line-height: 1;
    color: var(--brand-blue);
  }
</style>
</head>
<body>
  <main class="card">
    <svg class="brand-mark" viewBox="0 0 216 216" aria-hidden="true">
      <circle cx="108" cy="108" r="98" fill="none" stroke="var(--brand-green)" stroke-width="16"/>
    </svg>
    <div class="brand-name">Sunward Grid</div>

    <div class="person-name">Name</div>
    <div class="person-position">Position</div>

    <div class="rule rule--blue" style="top:727px"></div>
    <div class="address">
      Address: XXXXXXXXXXXX<br>
      XXXXXXXXXXXXXXXXXXX<br>
      XXXXXXXXXXXXXXXXXXX
    </div>
    <div class="rule rule--blue" style="top:904px"></div>

    <div class="rule rule--green" style="top:975px"></div>
    <div class="phone">Phone: XXX.XXX.XXXX</div>
    <div class="rule rule--green" style="top:1035px"></div>

    <div class="email">Email: XXXXXXXXX@xxxxxxx.com</div>
  </main>
</body>
</html>
```